Virtualization software: PowerPoint, business cards

We're a young, small, dynamic application virtualization company: www.velrinta.com
We need a PowerPoint template + business cards. PDF background will be a plus.
This is mostly for enterprise clients.
Clean, professional, and most of all - following our website's colors.

Reason: Busy weekend; we'll need some more time to provide feedback & choose.

Target Market(s)

Corporate clients & investors.

Industry/Entity Type

Business

Requirements
Must have
• Clean, professional, and following our website's look: www.velrinta.com

```html
<!DOCTYPE html>
<html lang="en">
<head>
<meta charset="utf-8">
<title>Velrinta Presentation Template</title>
<link rel="stylesheet" href="https://fonts.googleapis.com/css2?family=Exo+2:wght@400;500;600&display=swap">
<style>
  :root {
    --stage: #4a4a48;
    --frame: #e9e9e9;
    --header: #231f20;
    --band: rgba(40, 40, 40, 0.72);
    --white: #ffffff;
    --muted-white: #dcdcdc;
    --ink: #1e1e1e;
    --bullet: #2aa6e0;
    --photo-light: #e6e4e0;
    --photo-mid: #c9c2b8;
    --slide-light: #fafafa;
    --slide-edge: #c9c9c9;
    --bar-red: #e8392a;
    --bar-blue: #1f4fe0;
    --bar-green: #23a24a;
    --bar-yellow: #f1d420;
  }
  * { margin: 0; padding: 0; box-sizing: border-box; }
  html, body { width: 1200px; height: 849px; overflow: hidden; }
  body {
    position: relative;
    background: var(--stage);
    font-family: "Exo 2", "Segoe UI", sans-serif;
  }
  .slide { position: absolute; width: 561px; height: 420px; }

  /* Title slide */
  .slide--title { left: 28px; top: 32px; background: var(--frame); }
  .title-header {
    position: absolute; left: 29px; top: 23px; width: 501px; height: 65px;
    background: var(--header); border-radius: 6px 6px 0 0;
  }
  .brand {
    position: absolute; left: 21px; top: 16px;
    color: var(--white); font-weight: 400; font-size: 28px; letter-spacing: 2px;
  }
  .pointer { position: absolute; display: block; }
  .title-header .pointer { left: 47px; top: 65px; }
  .hero-photo {
    position: absolute; left: 29px; top: 88px; width: 501px; height: 310px;
    background: linear-gradient(110deg, var(--photo-mid) 0%, var(--photo-light) 45%, #f4f3f1 70%, var(--photo-mid) 100%);
  }
  .title-band {
    position: absolute; left: 29px; top: 323px; width: 501px; height: 51px;
    background: var(--band); padding: 6px 21px;
  }
  .title-band h1 {
    color: var(--white); font-weight: 600; font-size: 19px; line-height: 23px;
  }
  .title-band p { color: var(--muted-white); font-size: 12px; line-height: 16px; }

  /* Content slide */
  .slide--content {
    left: 614px; top: 393px;
    background: radial-gradient(ellipse at 55% 45%, var(--slide-light) 0%, #ececec 55%, var(--slide-edge) 100%);
  }
  .content-header {
    position: absolute; left: 29px; top: 22px; width: 502px; height: 66px;
    background: var(--header); border-radius: 6px 6px 0 0; padding: 11px 14px;
  }
  .content-header h2 { color: var(--white); font-weight: 600; font-size: 19px; line-height: 24px; }
  .content-header p { color: var(--muted-white); font-size: 13px; line-height: 17px; }
  .content-header .pointer { left: 47px; top: 66px; }

  .bullets {
    position: absolute; left: 44px; top: 110px; width: 262px;
    list-style: none; color: var(--ink); font-size: 13.5px; line-height: 20.2px;
  }
  .bullets li { position: relative; padding-left: 14px; }
  .bullets li::before {
    content: ""; position: absolute; left: 0; top: 8px;
    width: 4px; height: 4px; border-radius: 50%; background: var(--bullet);
  }
  .bullets ul { list-style: none; }
  .bullets ul li { margin-left: 0; }
  .bar-chart { position: absolute; left: 330px; top: 140px; }
  .footer-brand {
    position: absolute; right: 30px; bottom: 22px;
    color: var(--ink); font-weight: 400; font-size: 16px; letter-spacing: 1.5px;
  }
</style>
</head>
<body>

<section class="slide slide--title">
  <header class="title-header">
    <span class="brand">VELRINTA</span>
    <svg class="pointer" width="16" height="8" viewBox="0 0 16 8"><path d="M0 0H16L8 8Z" fill="#231f20"/></svg>
  </header>
  <div class="hero-photo" role="img" aria-label="Photo of a smiling woman lying on the floor using a laptop in a bright room"></div>
  <div class="title-band">
    <h1>Insert The Title of Your Presentation Here</h1>
    <p>Subtitle of the Presentation or main author’s name here</p>
  </div>
</section>

<section class="slide slide--content">
  <header class="content-header">
    <h2>Sample Slide Bullet Points</h2>
    <p>Placeholder for subtitle</p>
    <svg class="pointer" width="16" height="8" viewBox="0 0 16 8"><path d="M0 0H16L8 8Z" fill="#231f20"/></svg>
  </header>
  <ul class="bullets">
    <li>The text demonstrates how your own text will look when you replace the placeholder with your own text.
      <ul>
        <li>The text demonstrates how your own text will look when you replace the placeholder with your own text.</li>
        <li>The text demonstrates how your own text will look when you replace the placeholder with your own text.</li>
      </ul>
    </li>
  </ul>
  <svg class="bar-chart" width="204" height="180" viewBox="0 0 204 180" role="img" aria-label="Bar chart with four bars">
    <rect x="4" y="55" width="53" height="119" rx="3" fill="var(--bar-red)"/>
    <rect x="51" y="8" width="53" height="158" rx="3" fill="var(--bar-blue)"/>
    <rect x="106" y="26" width="46" height="132" rx="3" fill="var(--bar-green)"/>
    <rect x="153" y="55" width="46" height="96" rx="3" fill="var(--bar-yellow)"/>
  </svg>
  <span class="footer-brand">VELRINTA</span>
</section>

</body>
</html>
```